Business Card Design Project

WE NEED A CARD WITH THE NAME AND LOGO IN ONE SIDE AND THE ODER JUST THE INFORMATIONS LIKE NAME, E-MAIL, PHONE AND SITE. I HAVE A IDEA OF THE CARD ALL BLACK AND JUST COLLOORS IN THE LOGO AND INFORMATIONS. WE WANT SANTHING SIMPLE AND ELEGANT. SAMETHING NEW WICTH PASS CONFIANCE.
Updates

I HAVE UP DATE THE INFORMATIONS OF WAHT WE NEED. THNKSĀ 

Target Market(s)

COMPANY WHO ORGANIZE BIG CORPORATIVE EVENTS.

Industry/Entity Type

Business

Requirements
Should not have
• MUCH INFORMATION.

```html
<!DOCTYPE html>
<html lang="en">
<head>
<meta charset="utf-8">
<title>Nora Vance – Business Card</title>
<link rel="stylesheet" href="https://fonts.googleapis.com/css2?family=Cinzel:wght@600&family=Aldrich&family=Arimo:wght@400&display=swap">
<style>
  :root {
    --page-bg: #ffffff;
    --card-light: #e0dfdf;
    --ink-dark: #262a2d;
    --accent-blue: #1fade4;
    --panel-dark-top: #2c3034;
    --panel-dark-bottom: #1c1f22;
    --contact-text: #e6e8ea;
  }
  * { margin: 0; padding: 0; box-sizing: border-box; }
  html, body {
    width: 1200px;
    height: 900px;
    overflow: hidden;
    background: var(--page-bg);
  }
  .card {
    position: absolute;
    left: 110px;
    top: 148px;
    width: 980px;
    height: 603px;
    overflow: hidden;
  }
  .card__brand {
    position: absolute;
    inset: 0 0 auto 0;
    height: 298px;
    background: var(--card-light);
  }
  .brand__square {
    position: absolute;
    left: 62px;
    top: 100px;
    width: 150px;
    height: 150px;
    background: var(--ink-dark);
  }
  .brand__name {
    position: absolute;
    left: 286px;
    top: 118px;
    font-family: "Cinzel", serif;
    font-weight: 600;
    font-size: 104px;
    line-height: 1;
    color: var(--ink-dark);
    letter-spacing: 1px;
    white-space: nowrap;
  }
  .card__band {
    position: absolute;
    left: 0;
    right: 0;
    top: 298px;
    height: 33px;
    background: var(--accent-blue);
    display: flex;
    align-items: center;
    justify-content: center;
  }
  .band__title {
    font-family: "Aldrich", sans-serif;
    font-size: 25px;
    letter-spacing: 9.5px;
    color: var(--ink-dark);
    white-space: nowrap;
  }
  .card__contact {
    position: absolute;
    left: 0;
    right: 0;
    top: 331px;
    bottom: 0;
    background: linear-gradient(180deg, var(--panel-dark-top), var(--panel-dark-bottom));
    padding: 57px 0 0 56px;
    list-style: none;
  }
  .contact__item {
    display: flex;
    align-items: center;
    height: 47px;
    font-family: "Arimo", sans-serif;
    font-size: 35px;
    color: var(--contact-text);
    text-shadow: 0 2px 3px rgba(0, 0, 0, 0.8);
  }
  .contact__icon {
    width: 40px;
    height: 36px;
    margin-right: 6px;
    flex: none;
  }
</style>
</head>
<body>
  <section class="card" aria-label="Business card">
    <header class="card__brand">
      <div class="brand__square"></div>
      <h1 class="brand__name">Nora Vance</h1>
    </header>
    <div class="card__band">
      <p class="band__title">Telecom Broker/Business Trainer</p>
    </div>
    <ul class="card__contact">
      <li class="contact__item">
        <svg class="contact__icon" viewBox="0 0 40 36" aria-hidden="true">
          <path d="M4 12 Q20 0 36 12 L32 16 L27 13 L27 9 Q20 6 13 9 L13 13 L8 16 Z" fill="var(--accent-blue)"/>
          <path d="M10 16 L14 12 L26 12 L30 16 L32 32 L8 32 Z" fill="var(--accent-blue)"/>
          <rect x="15" y="18" width="10" height="10" fill="#1a7fa8"/>
        </svg>
        1-555.201.4870
      </li>
      <li class="contact__item">
        <svg class="contact__icon" viewBox="0 0 40 36" aria-hidden="true">
          <rect x="3" y="8" width="34" height="22" fill="none" stroke="var(--accent-blue)" stroke-width="2"/>
          <path d="M3 8 L20 22 L37 8 M3 30 L16 18 M37 30 L24 18" fill="none" stroke="var(--accent-blue)" stroke-width="2"/>
        </svg>
        nora.vance@mailbox.com
      </li>
      <li class="contact__item">
        <svg class="contact__icon" viewBox="0 0 40 36" aria-hidden="true">
          <g fill="none" stroke="var(--accent-blue)" stroke-width="2">
            <circle cx="20" cy="18" r="15" fill="var(--accent-blue)" fill-opacity="0.25"/>
            <ellipse cx="20" cy="18" rx="7" ry="15"/>
            <path d="M5 18 H35 M8 10 H32 M8 26 H32 M20 3 V33"/>
          </g>
        </svg>
        noravance.linkdirect.com
      </li>
    </ul>
  </section>
</body>
</html>
```